Teachers workshop flyer

I need a flyer to inform schools of a workshop for teachers that empowers the teacher to help traumatised and disadvantaged students to engage in successful learning.

I am a teacher and educator and my info for the flyer is attached.

Target Market(s)

Principals and vice-principals who have stressed staff and students and they want things to be better in the school!

Industry/Entity Type

Teacher

```html
<!DOCTYPE html>
<html lang="en">
<head>
<meta charset="utf-8">
<title>Brain-Based Strategies for Student Success</title>
<link href="https://fonts.googleapis.com/css2?family=Titan+One&family=Source+Sans+3:ital,wght@0,400;0,600;0,700;1,400&display=swap" rel="stylesheet">
<style>
  :root {
    --page: #ffffff;
    --panel: #f0f1f1;
    --blue: #0a6db5;
    --green: #6db33f;
    --ink: #2f2f2f;
    --muted: #555555;
    --dots: #9a9a9a;
    --photo-top: #ddd6d1;
    --photo-bottom: #ebe6e3;
  }
  * { margin: 0; padding: 0; box-sizing: border-box; }
  html, body { width: 846px; height: 1200px; overflow: hidden; background: var(--page); }
  .flyer { position: relative; width: 846px; height: 1200px; overflow: hidden; font-family: "Source Sans 3", Arial, sans-serif; color: var(--ink); }
  .photo-column { position: absolute; background: linear-gradient(180deg, var(--photo-top), var(--photo-bottom)); }
  .photo-column.left { left: 0; top: 60px; width: 160px; height: 1080px; }
  .photo-column.right { left: 683px; top: 80px; width: 163px; height: 1050px; }
  .panel { position: absolute; left: 155px; top: 30px; width: 533px; height: 1170px; background: var(--panel); box-shadow: 0 0 12px rgba(0,0,0,0.15); }
  .headline { position: absolute; top: 62px; left: 155px; width: 533px; text-align: center; font-family: "Titan One", "Arial Black", sans-serif; font-weight: 400; font-size: 60px; line-height: 62px; color: var(--blue); letter-spacing: 1px; text-shadow: 3px 3px 0 #fff, -3px -3px 0 #fff, 3px -3px 0 #fff, -3px 3px 0 #fff, 0 3px 0 #fff, 0 -3px 0 #fff, 3px 0 0 #fff, -3px 0 0 #fff, 5px 6px 6px rgba(0,0,0,0.35); }
  .intro { position: absolute; left: 185px; width: 475px; text-align: center; color: var(--green); font-weight: 700; font-size: 18.5px; line-height: 24px; }
  .intro.first { top: 336px; }
  .intro.second { top: 508px; }
  .divider { position: absolute; left: 175px; width: 495px; border: 0; border-top: 4px dotted var(--dots); opacity: .7; }
  .divider.upper { top: 684px; }
  .divider.lower { top: 1056px; }
  .details { position: absolute; left: 190px; width: 465px; top: 710px; text-align: center; font-size: 14.8px; line-height: 19.6px; }
  .details h2 { font-size: 14.8px; font-weight: 700; }
  .details .gap { margin-top: 19px; }
  .details .quote { font-style: italic; }
  .contact { position: absolute; left: 155px; width: 533px; top: 1078px; text-align: center; }
  .contact .phone { font-size: 21px; font-weight: 700; color: var(--blue); }
  .contact .note { font-size: 15px; color: var(--muted); margin-top: 2px; }
  .contact .web { font-size: 18px; font-weight: 700; color: var(--green); margin-top: 2px; }
</style>
</head>
<body>
<main class="flyer">
  <div class="photo-column left" role="img" aria-label="Photos of four smiling young adults peeking from behind the panel"></div>
  <div class="photo-column right" role="img" aria-label="Photos of four smiling young adults peeking from behind the panel"></div>

  <section class="panel"></section>

  <h1 class="headline">BRAIN-BASED<br>STRATEGIES<br>FOR STUDENT<br>SUCCESS</h1>

  <p class="intro first">Contemporary teaching is a highly complex role as increasing numbers of students attend school without the essential ‘self-skills’ to be truly ‘school-ready’ and successful. Instead these students often seek-out attention in ways that can disruptive in the classroom causing stress and frustration for teachers.</p>
  <p class="intro second">Dan shows how and why the most effective strategies for these students are guided by a sound understanding of child-development and brain-development - especially where trauma has left lasting impacts. Teachers can learn how to build a student’s self-skills, without the teacher having to become a therapist!</p>

  <hr class="divider upper">

  <section class="details">
    <h2>About the Presenter:</h2>
    <p><strong>Daniel Whitford</strong> is a Melbourne-based therapist and educator with over twenty years experience working with adults and young people in the area of trauma and recovery. Dan’s seminars are engaging and practical since teachers need effective strategies that will immediately translate into classroom practice. Dan has trained here and overseas in the most effective behavior change strategies.</p>
    <h2 class="gap">Teacher Feedback:</h2>
    <p class="quote">“Dan was such an engaging and energetic presenter whom I enjoyed immensely.  His presentation on the brain and take away strategies were so practical and meaningful. It was an invaluable session.”</p>
    <p class="quote gap">“My Light-bulb moments:<br>- I need to CONNECT – not correct – far more often.<br>- Seeing negative self-talk for what it is.<br>- Using far more ‘diversions’ in the avoidance loop.”</p>
  </section>

  <hr class="divider lower">

  <footer class="contact">
    <p class="phone">Call - 0491 570 156</p>
    <p class="note">for more information or to book Dan to come to your school visit:</p>
    <p class="web">www.danielwhitford.example/studentsuccess</p>
  </footer>
</main>
</body>
</html>
```